Vertical retractable banner/pop-up for conference

We need a banner for a personal tax business based in Luxembourg to use at conferences/presentations etc.

The company name is Morvane Tax & Consulting - please view the website www.morvanetax.example for the style of our business and use of colours.

The colours we use are:-
#7D1935
#4A96AD
#F5F3EE

Also uploaded are the logo files and the template from the printing company to ensure that the sizes/margins are correct.

Requirements
Must have
• Use of corporate colours (see above).
• Logo
• Website address
Nice to have
• We are open to ideas on style so do not want to prescribe too much as we would like to receive a variety of possible designs ranging from the more minimalist options to more detailed. Some considerations for the design could be to use:-
• 1) The tagline from the website - "Specialists in personal and expatriate taxation".
• 2) The website background is a picture of Luxembourg - if similar city pictures are used on the banner then they should be of Luxembourg also (i.e. not other cities).

```html
<!DOCTYPE html>
<html lang="en">
<head>
<meta charset="utf-8">
<title>Morvane Tax &amp; Consulting – Roll-up Banner</title>
<link rel="stylesheet" href="https://fonts.googleapis.com/css2?family=Questrial&family=Montserrat:wght@700;800&display=swap">
<style>
  :root {
    --maroon: #7D1935;
    --ink: #111111;
    --white: #ffffff;
    --stage: #f2f2f2;
    --ring: #8a8a8a;
    --photo-light: #d9d9d9;
    --photo-mid: #9a9a9a;
    --photo-dark: #3c3c3c;
  }
  * { margin: 0; padding: 0; box-sizing: border-box; }
  html, body {
    width: 874px;
    height: 1200px;
    overflow: hidden;
    background: var(--stage);
  }
  .canvas {
    position: relative;
    width: 874px;
    height: 1200px;
  }
  .banner {
    position: absolute;
    left: 199px;
    top: 40px;
    width: 476px;
    height: 1120px;
    background: var(--white);
    overflow: hidden;
    box-shadow: 0 6px 24px rgba(0,0,0,0.12);
  }

  /* Brand block */
  .brand-mark {
    position: absolute;
    left: 143px;
    top: 58px;
    width: 190px;
    height: 190px;
    border: 6px solid var(--ring);
    border-radius: 50%;
  }
  .brand-name {
    position: absolute;
    left: 0;
    top: 282px;
    width: 100%;
    text-align: center;
    font-family: "Questrial", sans-serif;
    font-weight: 400;
    color: var(--maroon);
    line-height: 1;
  }
  .brand-name .brand-line1 {
    display: block;
    font-size: 64px;
    letter-spacing: 1px;
  }
  .brand-name .brand-line2 {
    display: block;
    margin-top: 12px;
    font-size: 24px;
    letter-spacing: 1px;
  }

  /* City photograph area */
  .city-photo {
    position: absolute;
    left: 0;
    top: 380px;
    width: 100%;
    height: 740px;
    background:
      linear-gradient(180deg, var(--photo-light) 0%, var(--photo-mid) 35%, #7d7d7d 60%, var(--photo-mid) 80%, var(--photo-dark) 100%);
  }
  .header-curve {
    position: absolute;
    left: 0;
    top: 370px;
    width: 476px;
    height: 110px;
  }

  /* Tagline */
  .tagline {
    position: absolute;
    left: 0;
    top: 500px;
    width: 100%;
    text-align: center;
    font-family: "Montserrat", sans-serif;
    line-height: 1;
  }
  .tagline .intro {
    display: block;
    font-weight: 700;
    font-size: 34px;
    color: var(--ink);
    text-shadow: 0 0 6px rgba(255,255,255,0.9);
  }
  .tagline .focus {
    display: block;
    font-weight: 800;
    color: var(--maroon);
    text-shadow: 3px 3px 0 var(--white), -1px -1px 0 var(--white);
    letter-spacing: -1px;
  }
  .tagline .personal { font-size: 64px; margin-top: 14px; }
  .tagline .amp {
    display: block;
    font-weight: 800;
    font-size: 28px;
    color: var(--ink);
    margin-top: 4px;
    text-shadow: 0 0 6px rgba(255,255,255,0.9);
  }
  .tagline .expat { font-size: 56px; margin-top: 4px; }
  .tagline .taxation { font-size: 64px; margin-top: 4px; }

  /* Web address band */
  .web-band {
    position: absolute;
    left: 0;
    top: 880px;
    width: 100%;
    height: 78px;
    background: rgba(255,255,255,0.82);
    display: flex;
    align-items: center;
    justify-content: center;
    font-family: "Montserrat", sans-serif;
    font-weight: 700;
    font-size: 27px;
    color: var(--ink);
    letter-spacing: 0.5px;
  }

  .footer-band {
    position: absolute;
    left: 0;
    bottom: 0;
    width: 100%;
    height: 70px;
    background: linear-gradient(180deg, #2a2a2a, #141414);
  }
</style>
</head>
<body>
<div class="canvas">
  <div class="banner">
    <div class="city-photo" role="img" aria-label="Black-and-white photograph of Luxembourg City old town, rooftops and fortification walls"></div>

    <svg class="header-curve" viewBox="0 0 476 110" aria-hidden="true">
      <path d="M0 0 H476 V20 Q238 150 0 20 Z" fill="#ffffff"/>
      <path d="M0 20 Q238 150 476 20" fill="none" stroke="#cfcfcf" stroke-width="3"/>
    </svg>

    <div class="brand-mark" aria-hidden="true"></div>
    <h1 class="brand-name">
      <span class="brand-line1">MORVANE</span>
      <span class="brand-line2">TAX &amp; CONSULTING</span>
    </h1>

    <p class="tagline">
      <span class="intro">Specialists in</span>
      <span class="focus personal">PERSONAL</span>
      <span class="amp">&amp;</span>
      <span class="focus expat">EXPATRIATE</span>
      <span class="focus taxation">TAXATION</span>
    </p>

    <div class="web-band">www.morvanetax.example</div>
    <div class="footer-band"></div>
  </div>
</div>
</body>
</html>
```